Ravel Oversight Partners - Statonery Design

I just completed a redesign of my business card. Please do not design a logo or business card. See my current stationery design attached.

Target Market(s)

VP of Human Resources and Finance - Companies with 100 employees to 10,000

Industry/Entity Type

Business Consultant

Requirements
Must have
• Use the letterhead instructions for the color and fonts.

```html
<!DOCTYPE html>
<html lang="en">
<head>
<meta charset="utf-8">
<title>Ravel Oversight Partners – Stationery</title>
<link rel="stylesheet" href="https://fonts.googleapis.com/css2?family=Crimson+Text:wght@400&family=Raleway:wght@300;400&family=Roboto:wght@500&display=swap">
<style>
  :root {
    --plum: #6b1d45;
    --paper: #fbfbfb;
    --ink: #4a4a4a;
    --ink-soft: #6a6a6a;
    --label: #f2f2f2;
    --bg-dark: #8c8c8c;
    --bg-light: #b9b9b9;
  }
  * { box-sizing: border-box; margin: 0; padding: 0; }
  html, body { width: 1200px; height: 677px; overflow: hidden; }
  body {
    position: relative;
    background: linear-gradient(160deg, var(--bg-dark) 0%, #a3a3a3 55%, var(--bg-light) 100%);
    font-family: "Raleway", sans-serif;
  }
  .sheet {
    position: absolute;
    background: var(--paper);
    box-shadow: 0 1px 4px rgba(0,0,0,.25);
  }
  .letter { top: 74px; width: 369px; height: 521px; }
  .letter-one { left: 58px; }
  .letter-two { left: 451px; }

  .brand { position: absolute; text-align: center; white-space: nowrap; }
  .brand-mark { display: block; margin: 0 auto; border-radius: 50%; background: var(--plum); }
  .brand-name {
    display: block;
    font-family: "Crimson Text", serif;
    color: #444;
  }
  .letter .brand { top: 31px; width: 150px; margin-left: -75px; }
  .letter .brand-mark { width: 27px; height: 27px; }
  .letter .brand-name { font-size: 10px; margin-top: 6px; }
  .letter-one .brand { left: 76px; }
  .letter-two .brand { left: 185px; }

  .rule-v { position: absolute; width: 1px; background: var(--plum); }
  .contact {
    position: absolute;
    font-family: "Crimson Text", serif;
    font-size: 7.6px;
    line-height: 9px;
    color: var(--ink);
  }
  .letter-one .rule-a { left: 144px; top: 43px; height: 26px; }
  .letter-one .rule-b { left: 261px; top: 43px; height: 26px; }
  .letter-one .address { left: 163px; top: 41px; }
  .letter-one .phones { left: 278px; top: 41px; }

  .body-copy { position: absolute; left: 22px; top: 154px; width: 326px; color: var(--ink); }
  .salutation { font-size: 10.5px; font-weight: 300; margin-bottom: 15px; }
  .body-copy p { font-size: 5.8px; line-height: 8.4px; color: var(--ink-soft); margin-bottom: 8px; text-align: justify; }
  .body-copy .sign-off { margin-top: 14px; }
  .signature { display: block; width: 46px; height: 16px; margin-top: 8px; background: linear-gradient(90deg, #d9d9d9, #ececec); }

  .footer { position: absolute; left: 27px; right: 27px; top: 493px; display: flex; align-items: center; gap: 4px; }
  .footer .line { flex: 1; height: 1px; background: var(--plum); }
  .footer .web {
    font-family: "Crimson Text", serif;
    font-size: 8.2px;
    letter-spacing: 1px;
    color: var(--plum);
  }

  .envelope { width: 300px; height: 134px; }
  .envelope-back { left: 848px; top: 283px; overflow: hidden; }
  .envelope-back svg { position: absolute; inset: 0; }
  .envelope-front { left: 846px; top: 462px; }
  .envelope-front .brand { left: 55px; top: 18px; width: 110px; margin-left: -55px; }
  .envelope-front .brand-mark { width: 19px; height: 19px; }
  .envelope-front .brand-name { font-size: 7.4px; margin-top: 5px; }
  .envelope-front .rule-v { left: 101px; top: 23px; height: 23px; }
  .envelope-front .address { left: 110px; top: 21px; font-size: 6.6px; line-height: 8px; }

  .label {
    position: absolute;
    font-family: "Roboto", sans-serif;
    font-weight: 500;
    font-size: 9.6px;
    letter-spacing: .3px;
    color: var(--label);
    text-align: center;
    width: 300px;
  }
</style>
</head>
<body>

<section class="sheet letter letter-one">
  <div class="brand">
    <span class="brand-mark"></span>
    <span class="brand-name">Ravel Oversight Partners</span>
  </div>
  <span class="rule-v rule-a"></span>
  <div class="contact address">1180 Harbor Lane NE<br>Suite 210<br>Lakeview, MI 49601</div>
  <span class="rule-v rule-b"></span>
  <div class="contact phones">555.214.7780 (main)<br>555.214.7782 (direct)<br>555.214.7789 (Fax)</div>

  <div class="body-copy">
    <div class="salutation">Dear Mr. Hale,</div>
    <p>Thank you for meeting with our team last week to review your workforce policies. We have outlined the key findings below along with the next steps we recommend for your leadership group. Our aim is to keep every review clear, fair and easy to act on.</p>
    <p>Our audit covered payroll records, benefit plans and hiring files across all regional offices. Most areas meet current standards, though a few records need updated signatures and clearer retention dates before the next reporting cycle.</p>
    <p>We suggest a short training session for managers on leave requests and overtime rules. This can be held on site or online, and we will provide written guides for each department so staff have a simple reference at hand.</p>
    <p>Please review the attached summary and let us know a convenient time to discuss the plan. We look forward to working with you.</p>
    <p class="sign-off">Sincerely,</p>
    <span class="signature" role="img" aria-label="Handwritten signature"></span>
  </div>

  <div class="footer"><span class="line"></span><span class="web">WWW.RAVELOVERSIGHT.COM</span><span class="line"></span></div>
</section>
<div class="label" style="left:92px;top:611px;">LETTER PAGE 1</div>

<section class="sheet letter letter-two">
  <div class="brand">
    <span class="brand-mark"></span>
    <span class="brand-name">Ravel Oversight Partners</span>
  </div>
  <div class="footer"><span class="line"></span><span class="web">WWW.RAVELOVERSIGHT.COM</span><span class="line"></span></div>
</section>
<div class="label" style="left:486px;top:611px;">LETTER PAGE 2</div>

<section class="sheet envelope envelope-back">
  <svg width="300" height="134" viewBox="0 0 300 134" aria-hidden="true">
    <line x1="0" y1="134" x2="135" y2="58" stroke="#e6e6e6" stroke-width="1"/>
    <line x1="300" y1="134" x2="165" y2="58" stroke="#e6e6e6" stroke-width="1"/>
    <path d="M0 0 H300 L170 72 Q156 80 142 72 Z" fill="var(--plum)"/>
    <circle cx="156" cy="36" r="12.5" fill="#fff"/>
  </svg>
</section>
<div class="label" style="left:848px;top:435px;">ENVELOPE BACK</div>

<section class="sheet envelope envelope-front">
  <div class="brand">
    <span class="brand-mark"></span>
    <span class="brand-name">Ravel Oversight Partners</span>
  </div>
  <span class="rule-v"></span>
  <div class="contact address">1180 Harbor Lane NE<br>Suite 210<br>Lakeview, MI 49601</div>
</section>
<div class="label" style="left:846px;top:611px;">ENVELOPE FRONT</div>

</body>
</html>
```